New look modernised front page for Marlowe Lawn Sports Guild Website Which incorporates our new logo (to be provided as a png file)
We want the home page to a panel to allow an image rotator and provide ready access to links to other inflation via some link menus/panel/button
1. Join a Croquet Club - links to details about Croquet in NSW - gateway to information of interest or the general public/“interested others” eg about the game, clubs locations and contacts
2. Club and Member Information - newsletters, Calender of events, and downloads
3. Officials and volunteers - training resources etc
4. Member and Club sign in - access to database
5. About Us - information about Marlowe Lawn Sports Guild incorporated -peak body for croquet in NSW - governance, contact details etc

Current website is at https://www.marlowe-guild.org/index.html

Target Market(s)

Dual target - People interested in learning about croquet and existing members

Number of Pages Required

1 page

Font styles to use
Sans Serif

Colors
0255a3
3377b5
85acd3
85cae6
33a6d7
0792cd
00a990

Requirements
Must have
• Contemporary feel
• Include logo - file attached
• Colours to include blues which are the NSW colour
Nice to have
• We want the home page to a panel to allow an image rotator and provide ready access to links to other inflation via some link menus/panel/button
• 1. Join a Croquet Club - links to details about Croquet in NSW - gateway to information of interest or the general public/“interested others” eg about the game, clubs locations and contacts
• 2. Club and Member Information - newsletters, Calender of events, and downloads
• 3. Officials and volunteers - training resources etc
• 4. Member and Club sign in - access to database
• 5. About Us - information about Marlowe Lawn Sports Guild incorporated -peak body for croquet in NSW - governance, contact details etc
• Want to have feeling of activity/movement/alive
• Current website is at https://www.marlowe-guild.org/index.html
• Some photos attached for information

```html
<!DOCTYPE html>
<html lang="en">
<head>
<meta charset="utf-8">
<title>Marlowe Lawn Sports Guild — Home</title>
<link rel="stylesheet" href="https://fonts.googleapis.com/css2?family=Oswald:wght@400;500;600&family=Montserrat:wght@400;500;600&display=swap">
<style>
:root{
  --blue-deep:#0255a3;
  --blue-mid:#3377b5;
  --blue-soft:#85acd3;
  --blue-sky:#85cae6;
  --blue-bright:#33a6d7;
  --blue-vivid:#0792cd;
  --teal:#00a990;
  --ink:#1d1d1d;
  --text-grey:#9a9a9a;
  --footer-dark:#2b2b2b;
  --footer-darker:#232323;
  --footer-base:#1a1a1a;
  --white:#ffffff;
}
*{box-sizing:border-box;margin:0;padding:0}
html,body{width:1200px;height:3180px;overflow:hidden}
body{position:relative;background:var(--white);font-family:"Montserrat",Arial,sans-serif;color:var(--ink)}
.abs{position:absolute}
.heading{font-family:"Oswald",Arial,sans-serif}

/* top navigation */
.top-nav{left:0;top:0;width:1200px;height:42px;background:var(--white)}
.top-nav ul{position:absolute;left:161px;top:0;width:761px;height:42px;list-style:none;display:flex;justify-content:space-between;align-items:center}
.top-nav li{font-size:10px;font-weight:600;text-transform:uppercase;color:var(--ink);position:relative;white-space:nowrap}
.top-nav li.is-active::before{content:"";position:absolute;left:0;right:0;top:-15px;height:3px;background:var(--blue-deep)}
.top-nav .sign-in{position:absolute;left:973px;top:0;width:64px;height:42px;background:var(--blue-vivid);color:var(--white);font-size:10px;font-weight:600;display:flex;align-items:center;justify-content:center}

/* hero */
.hero{left:0;top:42px;width:1200px;height:594px;background:linear-gradient(180deg,#6b8a55 0%,#a9b08a 35%,#d9d2bd 62%,#c8bfa4 100%)}
.hero-title{left:0;top:190px;width:1200px;text-align:center;color:var(--white);font-size:40px;font-weight:500;letter-spacing:.5px}
.hero-welcome{left:339px;top:240px;width:526px;height:54px;background:var(--blue-deep);color:var(--white);font-size:33px;font-weight:400;display:flex;align-items:center;justify-content:center;letter-spacing:.3px;white-space:nowrap}
.hero-welcome span{font-size:26px}
.hero-sub{left:271px;top:318px;width:658px;height:47px;background:var(--blue-vivid);color:var(--white);font-size:14.5px;display:flex;align-items:center;justify-content:center}
.hero-btn{left:509px;top:414px;width:180px;height:42px;background:var(--white);color:var(--ink);font-size:10.5px;font-weight:600;display:flex;align-items:center;justify-content:center;text-transform:uppercase}
.hero-arrow{top:266px;width:34px;height:34px;border-radius:50%;background:#111;display:flex;align-items:center;justify-content:center}

/* secondary navigation */
.sub-nav{left:0;top:636px;width:1200px;height:36px;background:var(--blue-deep);border-bottom:3px solid var(--blue-vivid)}
.sub-nav ul{list-style:none;display:flex;justify-content:space-between;margin-left:244px;width:711px;height:100%;align-items:center}
.sub-nav li{font-size:10px;font-weight:600;color:var(--white);text-transform:uppercase}

/* join */
.join-title{left:197px;top:768px;width:120px;font-size:26px;font-weight:600;line-height:36px;text-transform:uppercase}
.join-rule{left:318px;top:748px;width:2px;height:146px;background:#dcdcdc}
.join-copy{left:335px;top:762px;width:660px;font-size:11px;line-height:20px;color:var(--text-grey)}
.outline-btn{border:2px solid var(--blue-deep);color:var(--blue-deep);font-size:10px;font-weight:600;display:flex;align-items:center;justify-content:center;text-transform:uppercase;background:var(--white)}
.join-btn{left:335px;top:840px;width:168px;height:34px}

/* feature panels */
.panel-blue{background:linear-gradient(120deg,var(--blue-vivid) 0%,var(--blue-bright) 45%,var(--blue-sky) 100%)}
.photo{background:linear-gradient(160deg,#2f4a30 0%,#6f7a55 40%,#8d906f 65%,#a9a487 100%)}
.feature-title{font-size:40px;font-weight:500;color:var(--white);letter-spacing:-.3px;white-space:nowrap}
.feature-copy{font-size:11px;line-height:21px;color:var(--white)}
.ghost-btn{border:2px solid var(--blue-deep);color:var(--white);font-size:10px;font-weight:600;display:flex;align-items:center;justify-content:center;text-transform:uppercase}

/* sign-in band */
.signin-frame{left:0;top:1478px;width:1200px;height:250px;background:#d8d8d8}
.signin-band{left:6px;top:1484px;width:1188px;height:238px;background:linear-gradient(100deg,var(--blue-deep) 0%,#0a5fb0 50%,var(--blue-deep) 100%)}
.signin-title{left:0;top:1530px;width:1200px;text-align:center;color:var(--white);font-size:29px;font-weight:500}
.signin-sub{left:0;top:1574px;width:1200px;text-align:center;color:var(--white);font-size:13px;font-weight:500}
.signin-input{left:318px;top:1626px;width:420px;height:42px;border:2px solid var(--white);border-right:none;color:var(--white);font-size:11px;padding-left:26px;display:flex;align-items:center}
.signin-btn{left:738px;top:1626px;width:142px;height:42px;border:2px solid var(--white);color:var(--white);font-size:11px;font-weight:600;display:flex;align-items:center;justify-content:center;gap:10px}

/* about */
.about-title{left:0;top:2330px;width:1200px;text-align:center;font-size:29px;font-weight:500;text-transform:uppercase}
.about-col{top:2392px;width:426px;font-size:10.5px;line-height:19px;color:var(--text-grey)}
.about-btn{left:541px;top:2500px;width:118px;height:38px}

/* footer */
.footer-top{left:0;top:2612px;width:1200px;height:246px;background:var(--footer-dark)}
.footer-brand{left:197px;top:2680px;width:220px;color:var(--white);font-size:26px;font-weight:500;line-height:30px;text-transform:uppercase}
.footer-rule{left:424px;top:2676px;width:3px;height:64px;background:var(--blue-vivid)}
.footer-about{left:445px;top:2678px;width:580px;font-size:11px;line-height:22px;color:#9b9b9b}
.contact{top:2790px;display:flex;align-items:flex-start;gap:10px;font-size:10px;line-height:18px;color:#a5a5a5;white-space:nowrap}
.socials{left:865px;top:2793px;display:flex;gap:7px}
.socials span{width:22px;height:22px;border:1px solid #8c8c8c}
.footer-links{left:0;top:2858px;width:1200px;height:280px;background:var(--footer-darker)}
.footer-heading{top:2900px;color:var(--white);font-size:13px;font-weight:500;text-transform:uppercase}
.footer-list{top:2934px;list-style:none;font-size:11px;line-height:22px;color:#8e8e8e}
.newsletter-copy{left:719px;top:2934px;width:320px;font-size:11px;line-height:22px;color:#8e8e8e}
.newsletter-input{left:719px;top:2996px;width:229px;height:34px;background:#3a3a3a;color:#bdbdbd;font-size:10.5px;padding-left:20px;display:flex;align-items:center}
.newsletter-btn{left:948px;top:2996px;width:89px;height:34px;background:var(--blue-deep);color:var(--white);font-size:10.5px;font-weight:600;display:flex;align-items:center;justify-content:center}
.copyright-bar{left:0;top:3138px;width:1200px;height:42px;background:var(--footer-base);font-size:10.5px;color:#9a9a9a}
.copyright-bar .left{position:absolute;left:161px;top:14px}
.copyright-bar .right{position:absolute;right:161px;top:14px}
</style>
</head>
<body>

<nav class="abs top-nav">
  <ul>
    <li class="is-active">Home</li><li>About</li><li>How to Play</li><li>Newsletter Clubs</li><li>Club News</li><li>Events</li><li>Results</li><li>Handicaps</li><li>Coaching</li>
  </ul>
  <div class="sign-in">SIGN IN</div>
</nav>

<section class="abs hero" role="img" aria-label="Rotating photo: four smiling croquet players in whites and hats standing on a lawn court"></section>
<div class="abs hero-title heading">MARLOWE LAWN SPORTS GUILD</div>
<div class="abs hero-welcome heading">WELCOME TO&nbsp;<span>MARLOWE LAWN SPORTS GUILD</span></div>
<div class="abs hero-sub">Croquet is a very old game that had its beginnings in the early 1400's community.</div>
<div class="abs hero-btn">Join a Croquet Club</div>
<div class="abs hero-arrow" style="left:127px"><svg width="12" height="12" viewBox="0 0 12 12"><path d="M8 1 3 6l5 5" fill="none" stroke="#fff" stroke-width="2"/></svg></div>
<div class="abs hero-arrow" style="left:1037px"><svg width="12" height="12" viewBox="0 0 12 12"><path d="M4 1l5 5-5 5" fill="none" stroke="#fff" stroke-width="2"/></svg></div>

<nav class="abs sub-nav">
  <ul><li>Refereeing</li><li>Equipment</li><li>Shop</li><li>Downloads</li><li>Governance</li><li>Links</li><li>Contact</li></ul>
</nav>

<section>
  <h2 class="abs join-title heading">Join a Croquet Club</h2>
  <div class="abs join-rule"></div>
  <p class="abs join-copy">Croquet is a game that can be played by people as young as 10 but it is an ideal game for those in the senior age group. It is one of the few games that can be played by people into their 80's and, with the population in Australia ageing, its popularity is growing. It can be played equally well by men and women.</p>
  <div class="abs outline-btn join-btn">Join a Croquet Club</div>
</section>

<section>
  <div class="abs panel-blue" style="left:0;top:1014px;width:943px;height:386px"></div>
  <div class="abs photo" role="img" aria-label="Photo: players in whites with mallets on a croquet lawn" style="left:511px;top:958px;width:689px;height:420px"></div>
  <h2 class="abs feature-title heading" style="left:159px;top:1088px">Club and Member Information</h2>
  <p class="abs feature-copy" style="left:159px;top:1168px;width:420px">Croquet is a very old game that had its beginnings in the early 1400's. Below is a brief history of the game. England developed the initial rules of the game in the mid 1800's and the game is now played in about 26 countries around the world. Australia was an early adopter of the game and now has about 8,000 players of which just under 3,000 are in NSW.</p>
  <div class="abs ghost-btn" style="left:159px;top:1304px;width:112px;height:36px">Learn More</div>
</section>

<section>
  <div class="abs signin-frame"></div>
  <div class="abs signin-band"></div>
  <h2 class="abs signin-title heading">MEMBER AND CLUB SIGN IN</h2>
  <p class="abs signin-sub">Croquet is a very old game that had its beginnings in the early 1400's community.</p>
  <div class="abs signin-input">Enter Your E-mail</div>
  <div class="abs signin-btn">SIGN IN
    <svg width="16" height="14" viewBox="0 0 16 14"><path d="M8 1 3 6h3v4h4V6h3z" fill="#fff"/><path d="M2 12h12" stroke="#fff" stroke-width="2"/></svg>
  </div>
</section>

<section>
  <div class="abs panel-blue" style="left:254px;top:1876px;width:946px;height:386px"></div>
  <div class="abs photo" role="img" aria-label="Photo: two croquet players shaking hands on the lawn, balls at their feet" style="left:0;top:1804px;width:689px;height:418px;background:linear-gradient(170deg,#2c3a2a 0%,#5f6446 35%,#7d7a5e 60%,#8f8a70 100%)"></div>
  <h2 class="abs feature-title heading" style="left:620px;top:1934px;width:419px;text-align:right">Officials and volunteers</h2>
  <p class="abs feature-copy" style="left:620px;top:2016px;width:419px;text-align:right">Croquet is a very old game that had its beginnings in the early 1400's. Below is a brief history of the game. England developed the initial rules of the game in the mid 1800's and the game is now played in about 26 countries around the world. Australia was an early adopter of the game and now has about 8,000 players of which just under 3,000 are in NSW.</p>
  <div class="abs ghost-btn" style="left:926px;top:2152px;width:112px;height:36px">Learn More</div>
</section>

<section>
  <h2 class="abs about-title heading">About Us</h2>
  <p class="abs about-col" style="left:165px">Marlowe Lawn Sports Guild is the State organisation responsible for promoting, organising and developing the sport of Croquet in NSW. It also is charged with maintaining uniform handicapping system and coordinating croquet activities throughout the state. The Guild is affiliated with, and a member of, the National Lawn Sports Council.</p>
  <p class="abs about-col" style="left:606px">The state organisation is managed by several specialist committees reporting to an Executive Committee with all decisions being ratified by a council consisting of delegates from individual croquet clubs. As at September 2011 there were 68 affiliated croquet clubs throughout the state with just under 3,000 members.</p>
  <div class="abs outline-btn about-btn">Learn More</div>
</section>

<footer>
  <div class="abs footer-top"></div>
  <div class="abs footer-brand heading">Marlowe Lawn Sports Guild</div>
  <div class="abs footer-rule"></div>
  <p class="abs footer-about">Croquet is a very old game that had its beginnings in the early 1400's. Below is a brief history of the game. England developed the initial rules of the game in the mid 1800's and the game is now played in about 26 countries around the world.</p>

  <div class="abs contact" style="left:197px">
    <svg width="20" height="18" viewBox="0 0 20 18"><path d="M10 1 1 9h3v8h5v-5h2v5h5V9h3z" fill="var(--blue-vivid)"/></svg>
    <span>Marlowe Lawn Sports Guild Inc,<br>Harlow Green, Brennan NSW 2099</span>
  </div>
  <div class="abs contact" style="left:434px">
    <svg width="20" height="20" viewBox="0 0 20 20"><path d="M5 2l3 4-2 2c1 3 3 5 6 6l2-2 4 3-2 3C9 18 2 11 2 4z" fill="none" stroke="var(--blue-vivid)" stroke-width="2"/></svg>
    <span>(02) 9000 4812<br>0400 123 987</span>
  </div>
  <div class="abs contact" style="left:610px">
    <svg width="24" height="16" viewBox="0 0 24 16"><rect x="1" y="1" width="22" height="14" fill="none" stroke="var(--blue-vivid)" stroke-width="2"/><path d="M1 1l11 8 11-8" fill="none" stroke="var(--blue-vivid)" stroke-width="2"/></svg>
    <span>Email : hello@marlowe-guild.org</span>
  </div>
  <div class="abs socials" aria-label="Social links"><span></span><span></span><span></span><span></span></div>

  <div class="abs footer-links"></div>
  <h3 class="abs footer-heading heading" style="left:161px">Navigation</h3>
  <ul class="abs footer-list" style="left:161px"><li>Home</li><li>About</li><li>How to Play</li><li>Newsletter</li><li>Clubs Club</li><li>News</li><li>Events</li></ul>
  <ul class="abs footer-list" style="left:346px"><li>Results</li><li>Handicaps</li><li>Coaching</li><li>Refereeing</li><li>Equipment</li><li>Shop</li></ul>
  <ul class="abs footer-list" style="left:524px"><li>Downloads</li><li>Governance</li><li>Links</li><li>Contact</li><li>Sign In</li></ul>
  <h3 class="abs footer-heading heading" style="left:719px">Subscribe the Newsletter</h3>
  <p class="abs newsletter-copy">Lorem Ipsum is simply dummy text of the printing and typesetting Ipsum has industry's</p>
  <div class="abs newsletter-input">Write Email Address</div>
  <div class="abs newsletter-btn">SUBSCRIBE</div>

  <div class="abs copyright-bar">
    <span class="left">Copyright 2018 © Marlowe Lawn Sports Guild</span>
    <span class="right">Terms and Condition</span>
  </div>
</footer>

</body>
</html>
```